Web Design Project - (DESIGN AND FOLLOW UP CODING)

Web design for new management consultancy company

**About The Hadley Collective

We work with organisations find and implement creative and sensible solutions...

We explore and inform…We have in-house research capability and enrich discussion through our own research, analysis and inputs. We interview staff and stakeholders, analyse data and literature and help you develop knowledge and solutions, and the plans to implement these.

We present new ideas…We develop proposals and reports that use internally and externally derived evidence to propose effective new solutions.

Specialties
Higher Education, TAFE, Local Government, Regional Development

Industry
Education Management
Updates

LOGO added to brief (or email me on mavenlink@quorix.com.au to get copy

Target Market(s)

Business and government managers

Industry/Entity Type

Education

Requirements
Must have
• Sections:

**About
We work with organisations find and implement solutions to opportunities and challenges.
We explore and inform…
We present new ideas…

We develop proposals and reports that link internally and externally derived evidence to develop and implement new solutions.

Our three practice pillars are-
Ideas and partnerships:
Knowledgeable leaders:
Solutions:

** People
Marcus Pellow (PHOTO) Bio

** Services
Acumen - Solutions - Partnerships -Implementation
- On time and within budget.
- Project leadership.
- Researched inputs and facilitated outcomes.
- Focus on implementation.
- Develop value-adding partnerships and get them funded
- Creative responses to funding opportunities
- Organisational reviews

Sectors
-Education
-State Government
- Local Government
- Utilities
- Financial services
- Health and ageing
- Human services
- Government
-Regional

** Careers

** Key Partners
With weblinks

** Contact

Links to Chirpline LinkedIn Friendbook
Nice to have
• Logo available from: mavenlink@quorix.com.au

```html
<!DOCTYPE html>
<html lang="en">
<head>
<meta charset="utf-8">
<title>The Hadley Collective — Management Consultancy</title>
<link href="https://fonts.googleapis.com/css2?family=Oswald:wght@400;500;600&family=Arimo:wght@400;700&family=Cinzel:wght@400&family=Open+Sans:wght@400&display=swap" rel="stylesheet">
<style>
:root{
  --blue:#0c6a9c;
  --blue-dark:#0b5a86;
  --orange:#f26532;
  --ink:#1c1c1c;
  --text:#333;
  --page:#f3f1f2;
  --rule:#9a9a9a;
  --grey-pill:#e2e2e2;
}
*{margin:0;padding:0;box-sizing:border-box}
html,body{width:692px;height:1200px;overflow:hidden}
body{background:var(--page);font-family:"Arimo",sans-serif;color:var(--text);position:relative}
.abs{position:absolute}

/* header */
.site-header{position:absolute;left:0;top:0;width:692px;height:96px;background:#fff}
.brand-name{left:42px;top:41px;font-family:"Oswald",sans-serif;font-weight:500;font-size:15px;color:var(--blue-dark);white-space:nowrap}
.nav a{position:absolute;font-family:"Oswald",sans-serif;font-weight:500;font-size:13.5px;color:var(--blue-dark);text-decoration:none;top:43px}
.nav .current{left:243px;top:0;width:76px;height:102px;background:var(--blue);color:#fff;text-align:center;padding-top:41px;font-size:15px}

/* hero */
.hero{left:0;top:96px;width:670px;height:217px;background:linear-gradient(180deg,#b9c2cb 0%,#d6dbe0 55%,#8f8e8c 80%,#6f6c68 100%)}
.hero-side{left:670px;top:117px;width:22px;height:196px;background:var(--blue)}
.hero-h{font-family:"Oswald",sans-serif;font-weight:600;color:#fff;line-height:1}
.hero-tag{left:176px;top:211px;width:158px;height:18px;background:var(--orange);color:#fff;font-size:8px;text-align:center;line-height:18px}

/* section heads */
.rule{height:1px;background:var(--rule)}
.section-title{font-family:"Oswald",sans-serif;font-weight:600;text-align:center;width:692px;left:0}

/* feature */
.bracket{border-color:var(--blue-dark);border-style:solid}
.feature-label{left:199px;top:421px;font-family:"Cinzel",serif;font-size:10.5px;color:var(--orange)}
.feature-body{left:202px;top:456px;width:392px;font-family:"Open Sans",sans-serif;font-size:7.2px;line-height:9.6px;color:#444}
.read-more{left:542px;top:528px;font-family:"Cinzel",serif;font-size:6px;color:var(--blue)}

/* columns */
.col-head{font-family:"Arimo",sans-serif;font-weight:700;font-size:13.5px;color:var(--ink);letter-spacing:.3px}
.col-text{font-size:10px;line-height:12px;color:var(--ink)}
.social-bar{left:45px;top:618px;width:156px;height:43px;background:linear-gradient(90deg,#d9d9d9,#ececec)}
.social-mail{left:45px;top:618px;width:32px;height:43px;background:var(--blue)}
.social-name{font-size:8px;font-weight:700;color:#222}
.reasons{left:237px;top:570px;width:206px;height:36px;background:var(--orange);color:#fff;display:flex;align-items:center;gap:14px;padding-left:36px}
.reasons b{font-size:17px}
.reasons span{font-size:7.5px;font-weight:700;letter-spacing:.3px}
.reasons-art{left:237px;top:611px;width:206px;height:146px;background:linear-gradient(160deg,#3fb8c9 0%,#2f8f8a 45%,#3b9a4a 70%,#e3d7a6 100%)}

/* people */
.person-tile{left:69px;top:960px;width:35px;height:40px;background:var(--orange);border-radius:6px 0 0 6px}
.person-pill{left:104px;top:960px;width:317px;height:40px;background:var(--grey-pill);border-radius:0 10px 10px 0}
.person-photo{left:101px;top:922px;width:108px;height:108px;border-radius:50%;background:linear-gradient(180deg,#d8cfc6,#5a5f6b);border:3px solid #a9a9a9}
.person-name{left:229px;top:971px;font-size:13px;font-weight:700;color:var(--blue-dark)}
.person-bio{font-size:9.6px;line-height:11px;color:var(--ink)}
.feedback-head{left:456px;top:931px;font-size:13.5px;font-weight:700;color:var(--ink);letter-spacing:.3px}
.avatar{width:40px;height:40px;border-radius:50%;border:2px solid #ddd;background:linear-gradient(180deg,#cfcfcf,#6b6b6b)}
.quote{font-size:8px;color:#222}
.quote-by{font-size:8px;color:var(--blue)}

/* footer */
.site-footer{left:0;top:1154px;width:692px;height:46px;background:var(--blue)}
.foot-nav a{position:absolute;top:1162px;font-size:8px;color:#fff;text-decoration:none}
.foot-sep{top:1154px;width:1px;height:22px;background:#d9e6ee}
</style>
</head>
<body>

<header class="site-header">
  <div class="abs brand-name">The Hadley Collective</div>
  <nav class="nav">
    <a class="current" href="#">HOME</a>
    <a style="left:341px" href="#">ABOUT</a>
    <a style="left:404px" href="#">SERVICES</a>
    <a style="left:482px" href="#">SECTORS</a>
    <a style="left:558px" href="#">CAREERS</a>
    <a style="left:618px" href="#">CONTACT US</a>
  </nav>
</header>

<section class="abs hero" role="img" aria-label="Photo of businessmen leaping between concrete blocks under a cloudy sky"></section>
<div class="abs hero-side"></div>
<div class="abs hero-h" style="left:133px;top:116px;font-size:21px">KEEP MOVING</div>
<div class="abs hero-h" style="left:188px;top:137px;font-size:11px">SOLVE YOUR</div>
<div class="abs hero-h" style="left:175px;top:164px;font-size:21px">PROBLEM</div>
<div class="abs hero-h" style="left:176px;top:188px;font-size:9px;color:#111">KEEP MOVING WITH US</div>
<div class="abs hero-tag">Management consultancy company</div>

<div class="abs rule" style="left:221px;top:345px;width:86px;background:#333"></div>
<div class="abs rule" style="left:333px;top:345px;width:93px;background:#333"></div>
<svg class="abs" style="left:317px;top:333px" width="12" height="22" viewBox="0 0 12 22"><path d="M6 0C2 0 0 3 0 6c0 4 4 5 5 16 1-7 7-11 7-16 0-3-2-6-6-6z" fill="var(--orange)"/></svg>
<h2 class="abs section-title" style="top:362px;font-size:21px;color:var(--blue-dark)">FIRST RECENTES</h2>

<div class="abs bracket" style="left:107px;top:422px;width:20px;height:20px;border-width:2px 0 0 2px"></div>
<div class="abs bracket" style="left:174px;top:514px;width:20px;height:20px;border-width:0 2px 2px 0;border-color:#222"></div>
<svg class="abs" style="left:117px;top:446px" width="55" height="65" viewBox="0 0 55 65">
  <circle cx="27.5" cy="14" r="13" fill="#2a2a2a"/>
  <path d="M0 44c0-10 7-15 16-15h23c9 0 16 5 16 15v21H0z" fill="#2a2a2a"/>
  <path d="M21 29h13l-6 24z" fill="#fff"/>
  <path d="M26 31h3l2 18-3 4-3-4z" fill="#2a2a2a"/>
  <rect x="38" y="51" width="9" height="2" fill="#fff"/>
</svg>
<div class="abs feature-label">FIRST ADDRESS</div>
<p class="abs feature-body">Harlow is NOT directly affiliated with the Relaymark project. He is an independent support consultant for Relaymark (and voice services in general to some degree). More importantly he is a great person and quite possibly greatest consultant there is out there, anywhere. Harlow is NOT directly affiliated with the Relaymark project. He is an independent support consultant for Relaymark (and voice services in general to some degree). More importantly he is a great person and quite possibly greatest consultant there is out there, anywhere..</p>
<div class="abs read-more">READ MORE</div>

<div class="abs rule" style="left:42px;top:569px;width:616px;background:#bbb"></div>

<h3 class="abs col-head" style="left:56px;top:589px">SOCIAL MEDIA</h3>
<div class="abs social-bar"></div>
<div class="abs social-mail"></div>
<svg class="abs" style="left:53px;top:633px" width="16" height="12" viewBox="0 0 16 12"><rect x=".5" y=".5" width="15" height="11" fill="#fff" stroke="#ccc"/><path d="M.5 .5l7.5 6 7.5-6" fill="none" stroke="#999"/></svg>
<span class="abs social-name" style="left:86px;top:635px">Chirpline</span>
<span class="abs social-name" style="left:128px;top:635px">Friendbook</span>
<svg class="abs" style="left:176px;top:632px" width="13" height="13" viewBox="0 0 13 13"><circle cx="2" cy="11" r="2" fill="#222"/><path d="M0 5a8 8 0 0 1 8 8M0 0a13 13 0 0 1 13 13" fill="none" stroke="#222" stroke-width="2.2"/></svg>
<h3 class="abs col-head" style="left:56px;top:679px">SOCIAL MEDIA</h3>
<p class="abs col-text" style="left:57px;top:704px;width:165px">Dummy data is benign informa-<br>tion that does not Dummy data<br>is benign informatioN.</p>

<div class="abs reasons"><b>3</b><span>REASONS TO CHOOSE US</span></div>
<div class="abs reasons-art" role="img" aria-label="Colourful illustration of a paper-craft island city with waves and an igloo"></div>
<h3 class="abs col-head" style="left:237px;width:206px;text-align:center;top:774px">IN OUR CENTER</h3>
<p class="abs col-text" style="left:237px;width:206px;text-align:center;top:794px;font-size:10.5px">Dummy data is benign information</p>
<svg class="abs" style="left:320px;top:815px" width="38" height="40" viewBox="0 0 38 40">
  <circle cx="19" cy="22" r="14" fill="none" stroke="var(--blue)" stroke-width="3.5"/>
  <path d="M19 13v10h7" fill="none" stroke="var(--blue)" stroke-width="2.5"/>
  <path d="M3 9a7 7 0 0 1 9-6M35 9a7 7 0 0 0-9-6" fill="none" stroke="var(--blue)" stroke-width="3"/>
  <path d="M10 36l-3 3M28 36l3 3" stroke="var(--blue)" stroke-width="3"/>
</svg>

<h3 class="abs col-head" style="left:494px;top:590px">OUR HELP FULL</h3>
<p class="abs col-text" style="left:496px;top:613px;width:165px">Dummy data is benign informa-<br>tion that does not Dummy data<br>is benign informatioN.</p>
<div class="abs" style="left:496px;top:674px;width:160px;border-top:1px dashed #bbb"></div>
<h3 class="abs col-head" style="left:494px;top:703px">WE CAN HELP OUT</h3>
<p class="abs col-text" style="left:494px;top:727px;width:165px">Dummy data is benign informa-<br>tion that does not Dummy data<br>is benign informatioN.</p>

<div class="abs rule" style="left:37px;top:842px;width:206px;background:#bbb"></div>
<div class="abs rule" style="left:451px;top:842px;width:203px;background:#bbb"></div>
<h2 class="abs section-title" style="top:863px;font-size:23px;color:var(--ink)">OUR PEOPLE</h2>
<div class="abs rule" style="left:267px;top:898px;width:140px;background:#555"></div>

<div class="abs person-tile"></div>
<div class="abs" style="left:81px;top:975px;width:10px;height:10px;border-radius:50%;background:#fff"></div>
<div class="abs person-pill"></div>
<div class="abs person-photo" role="img" aria-label="Portrait photo of Marcus Pellow"></div>
<div class="abs person-name">Name of man</div>
<p class="abs person-bio" style="left:200px;top:1023px;width:225px">Dummy data is benign information that does not Dummy data is benign informatioN.</p>
<p class="abs person-bio" style="left:101px;top:1047px;width:330px">Dummy data is benign information that does not Dummy data is benign informatioN.</p>

<h3 class="abs feedback-head">OUR CLIENTS FEEDBACK</h3>
<div class="abs avatar" style="left:461px;top:962px" role="img" aria-label="Client portrait photo"></div>
<span class="abs quote" style="left:509px;top:985px">I'd like it so much</span>
<span class="abs quote-by" style="left:586px;top:998px">John</span>
<div class="abs avatar" style="left:461px;top:1016px" role="img" aria-label="Client portrait photo"></div>
<span class="abs quote" style="left:509px;top:1038px">I'd like it so much</span>
<span class="abs quote-by" style="left:586px;top:1051px">John</span>
<div class="abs avatar" style="left:461px;top:1070px" role="img" aria-label="Client portrait photo"></div>
<span class="abs quote" style="left:509px;top:1093px">I'd like it so much</span>
<span class="abs quote-by" style="left:584px;top:1106px">John</span>

<footer class="abs site-footer"></footer>
<nav class="foot-nav">
  <a style="left:180px" href="#">HOME</a>
  <a style="left:243px" href="#">ABOUT</a>
  <a style="left:299px" href="#">SECTIONS</a>
  <a style="left:362px" href="#">SERVICES</a>
  <a style="left:428px" href="#">CAREERS</a>
  <a style="left:489px" href="#">CONTACT</a>
</nav>
<div class="abs foot-sep" style="left:221px"></div>
<div class="abs foot-sep" style="left:284px"></div>
<div class="abs foot-sep" style="left:348px"></div>
<div class="abs foot-sep" style="left:412px"></div>
<div class="abs foot-sep" style="left:475px"></div>
<svg class="abs" style="left:576px;top:1161px" width="8" height="8" viewBox="0 0 8 8"><path d="M0 4L4 0l4 4H7v4H1V4z" fill="#fff"/></svg>
<svg class="abs" style="left:593px;top:1160px" width="9" height="9" viewBox="0 0 9 9"><circle cx="3.5" cy="3.5" r="2.5" fill="none" stroke="#fff" stroke-width="1.3"/><path d="M5.5 5.5L8.5 8.5" stroke="#fff" stroke-width="1.5"/></svg>

</body>
</html>
```